Wound Care Flyer

Looking for a Trifold brochure that is modern and has a high aesthetic. (Specialty services) Would like the colors to center around Black and Gold. Possibly updating the logo. Attached is the old brochure and a document about our services.

```html
<!DOCTYPE html>
<html lang="en">
<head>
<meta charset="utf-8">
<title>Alderbrook Wounds – Trifold Brochure</title>
<link rel="stylesheet" href="https://fonts.googleapis.com/css2?family=Lato:ital,wght@0,400;0,700;1,400&family=Quicksand:wght@400;700&display=swap">
<style>
  :root{
    --black:#141414;
    --gold:#b8935c;
    --gold-light:#dcb98a;
    --gold-deep:#8a6a3c;
    --white:#ffffff;
    --backdrop:#9b9b9b;
  }
  html,body{margin:0;padding:0;width:1200px;height:2627px;overflow:hidden;background:var(--backdrop);}
  .brochure{position:absolute;left:40px;top:917px;width:1080px;height:764px;transform:scale(1.037);transform-origin:0 0;font-family:"Lato",sans-serif;color:var(--white);box-shadow:0 10px 30px rgba(0,0,0,.35);}
  .brochure-shapes{position:absolute;inset:0;}
  .panel{position:absolute;top:0;height:764px;width:360px;}
  .panel-why{left:0;}
  .panel-partner{left:360px;}
  .panel-cover{left:720px;}
  .heading-light{font-family:"Quicksand",sans-serif;font-weight:400;font-size:28px;text-align:center;margin:0;}
  .heading-bold{font-family:"Quicksand",sans-serif;font-weight:700;font-size:28px;text-align:center;margin:0;}
  .text-gold{color:var(--gold);}
  .rule{width:110px;height:1px;background:var(--white);margin:12px auto 0;opacity:.85;}
  .why-head{position:absolute;top:46px;width:100%;}
  .why-body{position:absolute;top:140px;width:100%;text-align:center;font-size:12.5px;line-height:16px;}
  .why-body p{margin:0 0 14px;}
  .benefits{list-style:none;margin:0 0 12px 66px;padding:0;text-align:left;}
  .benefits li{color:var(--gold);font-weight:700;font-size:15.5px;margin-bottom:14px;}
  .benefits li::before{content:"•";margin-right:5px;}
  .partner-head{position:absolute;top:46px;width:100%;}
  .services{position:absolute;top:148px;left:48px;right:20px;list-style:none;margin:0;padding:0;}
  .service{display:flex;align-items:flex-start;height:80px;}
  .service-icon{width:66px;height:66px;flex:none;margin-right:20px;margin-top:-2px;}
  .service h3{margin:2px 0 4px;font-size:12px;font-weight:700;}
  .service p{margin:0;font-size:12px;font-style:italic;line-height:15px;}
  .contact{position:absolute;top:528px;width:100%;text-align:center;}
  .contact h2{font-family:"Quicksand",sans-serif;font-size:26px;margin:0;color:var(--gold);}
  .contact h2 span{font-weight:400;}
  .contact .rule{width:80px;margin:8px auto 14px;}
  .contact-icon{width:28px;height:28px;display:block;margin:0 auto 6px;}
  .contact-line{margin:0;font-size:15px;line-height:20px;}
  .contact-email{margin-top:10px;}
  .brand-badge{position:absolute;width:156px;height:156px;display:flex;align-items:center;justify-content:center;text-align:center;font-family:"Lato",sans-serif;font-size:12px;letter-spacing:2px;line-height:16px;color:var(--gold);}
  .badge-why{left:209px;top:380px;}
  .badge-cover{left:80px;top:17px;}
  .cover-title{position:absolute;top:520px;width:100%;text-align:center;color:var(--gold);}
  .cover-title .kicker{font-family:"Quicksand",sans-serif;font-size:28px;margin:0;line-height:30px;}
  .cover-title .main{font-family:"Quicksand",sans-serif;font-weight:700;font-size:40px;margin:0;line-height:44px;}
  .tagline{border-top:1px solid var(--gold);border-bottom:1px solid var(--gold);margin:6px 42px 0;padding:5px 0;font-style:italic;font-size:13px;color:var(--white);}
  .features{position:absolute;top:660px;left:36px;right:36px;display:flex;list-style:none;margin:0;padding:0;}
  .feature{flex:1;text-align:center;font-size:11px;font-style:italic;line-height:13px;}
  .feature + .feature{border-left:1px solid #555;}
  .feature-icon{width:34px;height:34px;display:block;margin:0 auto 4px;}
</style>
</head>
<body>
<main class="brochure">
  <svg class="brochure-shapes" width="1080" height="764" viewBox="0 0 1080 764" aria-hidden="false">
    <defs>
      <linearGradient id="goldPanel" x1="0" y1="0" x2="1" y2="0">
        <stop offset="0" stop-color="#8f6e40"/><stop offset=".5" stop-color="#c9a06a"/><stop offset="1" stop-color="#e2bf8f"/>
      </linearGradient>
      <linearGradient id="goldRing" x1="0" y1="0" x2="1" y2="1">
        <stop offset="0" stop-color="#e8c996"/><stop offset=".5" stop-color="#a98350"/><stop offset="1" stop-color="#6e5430"/>
      </linearGradient>
      <linearGradient id="photoClinic" x1="0" y1="0" x2="1" y2="1">
        <stop offset="0" stop-color="#dfe3e6"/><stop offset=".5" stop-color="#7ea7d8"/><stop offset="1" stop-color="#e9e0d8"/>
      </linearGradient>
      <linearGradient id="photoNurse" x1="0" y1="0" x2="1" y2="1">
        <stop offset="0" stop-color="#f2eeea"/><stop offset=".5" stop-color="#4f86d6"/><stop offset="1" stop-color="#f1e3d8"/>
      </linearGradient>
      <clipPath id="clipWhy"><rect x="0" y="0" width="360" height="764"/></clipPath>
      <clipPath id="clipCover"><rect x="720" y="0" width="360" height="764"/></clipPath>
    </defs>
    <rect x="0" y="0" width="360" height="764" fill="var(--black)"/>
    <rect x="360" y="0" width="360" height="764" fill="url(#goldPanel)"/>
    <rect x="720" y="0" width="360" height="764" fill="var(--black)"/>

    <g clip-path="url(#clipWhy)">
      <circle cx="175" cy="690" r="295" fill="url(#goldRing)"/>
      <circle cx="175" cy="700" r="285" fill="var(--black)"/>
      <circle cx="185" cy="700" r="270" fill="url(#goldRing)"/>
      <circle cx="175" cy="705" r="262" fill="url(#photoClinic)" role="img" aria-label="Photo: gloved hands applying a bandage to a patient's arm"/>
    </g>

    <path d="M360 540 C440 490 560 470 640 495 C700 515 730 560 760 620 L760 764 L360 764 Z" fill="var(--black)"/>
    <path d="M360 540 C440 490 560 470 640 495 C700 515 730 560 760 620" fill="none" stroke="url(#goldRing)" stroke-width="3"/>

    <g clip-path="url(#clipCover)">
      <path d="M820 0 L1080 0 L1080 120 C1020 50 920 20 820 0 Z" fill="url(#goldRing)"/>
      <circle cx="965" cy="285" r="222" fill="url(#goldRing)"/>
      <circle cx="975" cy="280" r="207" fill="var(--black)"/>
      <circle cx="965" cy="282" r="198" fill="url(#goldRing)"/>
      <circle cx="975" cy="278" r="188" fill="url(#photoNurse)" role="img" aria-label="Photo: nurse in blue scrubs wrapping a bandage around a patient's hand"/>
    </g>

    <circle cx="287" cy="458" r="78" fill="var(--black)" stroke="url(#goldRing)" stroke-width="3"/>
    <circle cx="878" cy="95" r="78" fill="var(--black)" stroke="url(#goldRing)" stroke-width="3"/>
    <rect x="0" y="759" width="1080" height="5" fill="url(#goldRing)"/>
  </svg>

  <section class="panel panel-why">
    <header class="why-head">
      <h2 class="heading-light text-gold">Why Choose</h2>
      <h2 class="heading-bold text-gold">Alderbrook Wounds?</h2>
      <div class="rule"></div>
    </header>
    <div class="why-body">
      <p>Experience the highest standard of mobile<br>wound care, delivered directly to your home.</p>
      <p>We work side-by-side with your<br>physician to ensure:</p>
      <ul class="benefits">
        <li>Faster recovery</li>
        <li>Personalized treatment plans</li>
        <li>Superior patient comfort</li>
      </ul>
      <p>Our concierge-style approach empowers patients<br>to live healthier, happier lives.</p>
    </div>
    <div class="brand-badge badge-why">ALDERBROOK<br>WOUNDS</div>
  </section>

  <section class="panel panel-partner">
    <header class="partner-head">
      <h2 class="heading-light">Partner With</h2>
      <h2 class="heading-bold">Alderbrook Wounds</h2>
      <div class="rule"></div>
    </header>
    <ul class="services">
      <li class="service">
        <svg class="service-icon" viewBox="0 0 66 66"><circle cx="33" cy="33" r="32" fill="var(--black)"/><g fill="none" stroke="#fff" stroke-width="1.8"><circle cx="33" cy="25" r="7"/><path d="M20 48 C20 38 46 38 46 48 Z"/></g></svg>
        <div><h3>Enhanced Patient Outcomes</h3><p>Faster healing, reduced complications, and improved satisfaction.</p></div>
      </li>
      <li class="service">
        <svg class="service-icon" viewBox="0 0 66 66"><circle cx="33" cy="33" r="32" fill="var(--black)"/><g fill="none" stroke="#fff" stroke-width="1.8"><path d="M17 32 L33 18 L49 32 M21 29 V48 H45 V29"/><path d="M33 31 V43 M27 37 H39"/></g></svg>
        <div><h3>Extended Reach</h3><p>High-quality home-based care reduces unnecessary clinic visits.</p></div>
      </li>
      <li class="service">
        <svg class="service-icon" viewBox="0 0 66 66"><circle cx="33" cy="33" r="32" fill="var(--black)"/><g fill="none" stroke="#fff" stroke-width="1.8"><circle cx="28" cy="25" r="6"/><path d="M17 46 C17 36 39 36 39 46"/><circle cx="42" cy="42" r="5"/><path d="M44 20 L46 24 L50 24 L47 27 L48 31 L44 29 L40 31 L41 27 L38 24 L42 24 Z"/></g></svg>
        <div><h3>Professional Integrity</h3><p>Your patients receive care that reflects the highest standards.</p></div>
      </li>
      <li class="service">
        <svg class="service-icon" viewBox="0 0 66 66"><circle cx="33" cy="33" r="32" fill="var(--black)"/><g fill="none" stroke="#fff" stroke-width="1.8"><circle cx="33" cy="20" r="4"/><circle cx="21" cy="42" r="4"/><circle cx="45" cy="42" r="4"/><path d="M27 24 L23 34 M39 24 L43 34 M27 46 H39"/></g></svg>
        <div><h3>Seamless Collaboration</h3><p>We maintain open communication with all referring providers.</p></div>
      </li>
    </ul>
    <div class="contact">
      <h2>Contact <span>Us</span></h2>
      <div class="rule"></div>
      <svg class="contact-icon" viewBox="0 0 28 28"><circle cx="14" cy="14" r="13" fill="var(--gold)"/><path d="M9 8 L12 8 L13 11 L11 12.5 C12 15 13 16 15.5 17 L17 15 L20 16 L20 19 C14 20 8 14 9 8 Z" fill="var(--black)"/></svg>
      <p class="contact-line">(555) 014-2286</p>
      <p class="contact-line">(555) 014-7390</p>
      <svg class="contact-icon contact-email" viewBox="0 0 28 28"><circle cx="14" cy="14" r="13" fill="var(--gold)"/><rect x="8" y="10" width="12" height="9" fill="var(--black)"/><path d="M8 10 L14 15 L20 10" fill="none" stroke="var(--gold)" stroke-width="1.2"/></svg>
      <p class="contact-line">alderbrookwounds@example.com</p>
    </div>
  </section>

  <section class="panel panel-cover">
    <div class="brand-badge badge-cover">ALDERBROOK<br>WOUNDS</div>
    <header class="cover-title">
      <p class="kicker">MOBILE ADVANCED</p>
      <h1 class="main">WOUND CARE</h1>
      <p class="tagline">Compassionate. Convenient. Clinical Excellence.</p>
    </header>
    <ul class="features">
      <li class="feature">
        <svg class="feature-icon" viewBox="0 0 34 34"><g fill="none" stroke="var(--gold)" stroke-width="1.4"><circle cx="17" cy="17" r="16"/><path d="M11 22 L11 13 L15 13 L15 22 M15 16 L23 16 L23 22 L11 22"/></g></svg>
        Expert<br>in-home<br>wound care
      </li>
      <li class="feature">
        <svg class="feature-icon" viewBox="0 0 34 34"><g fill="none" stroke="var(--gold)" stroke-width="1.4"><circle cx="17" cy="17" r="16"/><path d="M17 24 V14 M17 18 C13 18 11 15 11 12 C15 12 17 14 17 18 M17 16 C21 16 23 13 23 10 C19 10 17 12 17 16"/></g></svg>
        Seamless<br>healing<br>journey
      </li>
      <li class="feature">
        <svg class="feature-icon" viewBox="0 0 34 34"><g fill="none" stroke="var(--gold)" stroke-width="1.4"><circle cx="17" cy="17" r="16"/><circle cx="17" cy="13" r="4"/><path d="M10 25 C10 18 24 18 24 25"/></g></svg>
        Serving<br>patients with<br>comfort
      </li>
    </ul>
  </section>
</main>
</body>
</html>
```